Minimalist Professional Business Card Design

We will be revamping our marketing materials: Business cards, Website and Catalogs.
Our Overall Design direction is to have a Minimalist artwork with Professionalism and Premium feel. The revamp starts with the new business card design followed by the others. Thus the designer whom work is selected for this job will likely to follow through with the subsequent jobs.

Target Market(s)

Upscale

Industry/Entity Type

Manufacturing

Contact Information for Business Card

For the Business Cards, the following are required:
. Minimalist yet Professional and Premium Feel
. Background Colors: white and / or light pastel yellow and if needed to smoothen the yellow, the light grey can be incorporated. We are changing our corporate bright yellow to either one of the three alternatives:
1. Soylant yellow CMYK (1%, 0%, 52%, 3%)
2. Popcorn yellow CMYK (0%, 0%, 33%, 0%)
3. Papaya yellow CMYK (0%, 0%, 51%, 0%)

Information to be inputed in the business cards:

Name: Barlen Moritova
Position: Managing Director

Company's name: Vellomar Valves Pte. Ltd.
Address: 512 Halvick Lane #07-09B
Singapore 617302
Tel: (65) 6281 4096
Fax: (65) 6294 7118
Email: barlen@vellomarvalves-example.com
Website: www.vellomarvalves-example.com
Skype: Vellomar.Valves
Whatsapp/ Line/ Viber/ WeChat: (65) 9372 6081

Company's Logo
Company's Slogan
Two product photos placed side by side (if this gets into the way of the design, it is OK not to include them)

Font styles to use
Serif

Colors
ffffff

Requirements
Must have
• Minimalist
Should not have
• Messy, crowded, playful

```html
<!DOCTYPE html>
<html lang="en">
<head>
<meta charset="utf-8">
<title>Vellomar Valves Business Card</title>
<link href="https://fonts.googleapis.com/css2?family=Roboto:wght@400;500;700;900&family=Courgette&display=swap" rel="stylesheet">
<style>
  :root {
    --backdrop: #e6e6e4;
    --pastel-yellow: #fbf4a3;
    --pale-yellow: #fdf9cf;
    --card-white: #ffffff;
    --ink: #4a4a4a;
    --ink-soft: #5c5c5c;
    --steel-light: #eef0f1;
    --steel-dark: #b9bec2;
  }
  * { margin: 0; padding: 0; box-sizing: border-box; }
  html, body {
    width: 1200px; height: 902px; overflow: hidden;
    background: var(--backdrop);
    font-family: "Roboto", Arial, sans-serif;
    color: var(--ink);
  }
  .canvas { position: relative; width: 1200px; height: 902px; }
  .card {
    position: absolute; width: 640px; height: 404px;
    border-radius: 28px; overflow: hidden;
    box-shadow: 0 6px 18px rgba(0,0,0,0.18);
  }
  /* Front */
  .card-front { left: 50px; top: 36px; background: var(--pastel-yellow); }
  .product-photo {
    position: absolute; border-radius: 10px;
    background: linear-gradient(90deg, var(--steel-dark), var(--steel-light) 45%, var(--steel-dark));
  }
  .product-left { left: 48px; top: 150px; width: 82px; height: 236px; }
  .product-right { right: 44px; top: 22px; width: 62px; height: 206px; }
  .front-brand {
    position: absolute; left: 190px; top: 112px; width: 300px;
    display: flex; flex-direction: column; align-items: center;
  }
  .brand-dot {
    width: 70px; height: 70px; border-radius: 50%; background: var(--ink);
    margin-bottom: 14px;
  }
  .brand-name {
    font-weight: 900; font-size: 46px; letter-spacing: 1px;
    color: var(--ink); line-height: 1;
  }
  .slogan {
    position: absolute; left: 150px; right: 120px; top: 300px; text-align: center;
    font-family: "Courgette", cursive; font-size: 20px; color: var(--ink-soft);
  }
  /* Back */
  .card-back {
    left: 510px; top: 462px;
    background: linear-gradient(160deg, var(--card-white) 20%, var(--pale-yellow) 60%, var(--pastel-yellow));
  }
  .back-brand {
    position: absolute; left: 34px; top: 112px;
    font-weight: 900; font-size: 50px; letter-spacing: 1px; line-height: 1;
  }
  .divider { position: absolute; height: 1px; background: var(--ink); }
  .divider-top { left: 300px; right: 34px; top: 196px; }
  .divider-bottom { left: 34px; width: 240px; top: 300px; }
  .person { position: absolute; left: 34px; top: 190px; line-height: 1.2; }
  .person-name { font-weight: 700; font-size: 18px; letter-spacing: 0.5px; }
  .person-role { font-size: 15px; }
  .company { font-weight: 700; font-size: 15px; margin-top: 8px; }
  .address { font-size: 14px; }
  .contact-list {
    position: absolute; left: 34px; top: 312px; list-style: none;
    font-size: 15px; line-height: 1.45;
  }
  .contact-list li, .online-list li { display: flex; align-items: center; gap: 8px; }
  .contact-list svg { width: 14px; height: 14px; fill: var(--ink); flex: none; }
  .online-list {
    position: absolute; right: 34px; top: 210px; list-style: none;
    font-size: 14px; line-height: 1.55; text-align: right;
  }
  .online-list li { justify-content: flex-end; }
  .icon-dot { width: 13px; height: 13px; border-radius: 50%; background: var(--ink); display: inline-block; flex: none; }
</style>
</head>
<body>
<main class="canvas">
  <section class="card card-front">
    <div class="product-photo product-left" role="img" aria-label="Stainless steel submersible pump photo"></div>
    <div class="product-photo product-right" role="img" aria-label="Stainless steel pump motor photo"></div>
    <div class="front-brand">
      <span class="brand-dot"></span>
      <span class="brand-name">VELLOMAR</span>
    </div>
    <p class="slogan">Built Strong | Made To Endure</p>
  </section>

  <section class="card card-back">
    <div class="back-brand">VELLOMAR</div>
    <div class="divider divider-top"></div>
    <div class="person">
      <p class="person-name">BARLEN MORITOVA</p>
      <p class="person-role">Managing Director</p>
      <p class="company">Vellomar Valves Pte. Ltd.</p>
      <p class="address">512 Halvick Lane #07-09B, Singapore 617302</p>
    </div>
    <div class="divider divider-bottom"></div>
    <ul class="contact-list">
      <li><svg viewBox="0 0 24 24"><path d="M6.6 10.8a15 15 0 0 0 6.6 6.6l2.2-2.2c.3-.3.7-.4 1-.2 1.1.4 2.3.6 3.6.6.6 0 1 .4 1 1V20c0 .6-.4 1-1 1A17 17 0 0 1 3 4c0-.6.4-1 1-1h3.5c.6 0 1 .4 1 1 0 1.3.2 2.5.6 3.6.1.3 0 .7-.2 1z"/></svg>(65) 6281 4096</li>
      <li><svg viewBox="0 0 24 24"><path d="M6 3h12v5H6zM4 9h16a2 2 0 0 1 2 2v6h-4v4H6v-4H2v-6a2 2 0 0 1 2-2zm4 7v3h8v-3z"/></svg>(65) 6294 7118</li>
      <li><svg viewBox="0 0 24 24"><path d="M2 5h20v14H2zm2 2v.5l8 5 8-5V7zm0 2.8V17h16V9.8l-8 5z"/></svg>barlen@vellomarvalves-example.com</li>
    </ul>
    <ul class="online-list">
      <li>www.vellomarvalves-example.com <span class="icon-dot"></span></li>
      <li>Vellomar.Valves <span class="icon-dot"></span></li>
      <li>(65) 9372 6081 <span class="icon-dot"></span></li>
    </ul>
  </section>
</main>
</body>
</html>
```